Design a Striking Charity Infographic for the Displaced Meal Pledge

Design a striking infographic to share online and raise awareness of the Meal Pledge.

This is a charity project that raises funds to provide refugees with the food, medicine and support they need to survive.

Your design should include the text and ingredients outlined below.

The infographic should be a strong visual statement that’s easy to share on social media such as Snapgrid, Chirpline and Friendwall.

The headline, ingredients and call to action 'Take the Kind Harbor Meal Pledge, June 19-25'

Text:
Headline: “Could you live on this much food for 1 week?”
Rice 1920g
Flour 400g
Lentils 170g
Dried chick peas 85g
Tinned sardines 125g
Tinned kidney beans 400g
Vegetable Oil 300ml

Take the Kind Harbor Meal Pledge, June 19-25
Sign up at www.mealpledgeweek.org.au
(this section with the web address needs to be very clear and easy to see in the graphic)

Footer text - note this section should not dominate, it's a teriary section of the design.
(1) Kind Harbor / Meal Pledge logo
(2) Design by PixelGuild (logo attached)

This copy needs to appear somewhere (very small) “The international aid agency of the Federated Assembly of Parishes. ABN 17 826 305 462”

Technical spec:
Imagery: photos are permitted; custom illustrations encouraged!
Size: maximum 1080x1080px
File size smaller than 5 MB
Colour ratios: Blue and White (80%), tertiary is red; see guide for more details

If the main image is full bleed you can stick headline copy, logos etc on top of it. Put body copy on a grunge brush.

If the images are not full bleed, use a blue background image (rice bag or paper) for the background. Put all the images in a frame. And fasten them on with a fastener (e.g. staple). Make the proportions of the frames / backgrounds / fasteners look realistic.

Logo:
Use the Meal Pledge stamp (larger) and Kind Harbor logo (smaller) on everything. Unless it’s on a plain white background use the sicker version of the KH logo.

Typography:
Veneer 2 for headlines
Caecelia is for body copy in print / on posters / on images put headline and body copy on a grunge brush
Remington Noiseless - use sparingly for personality elements, not for body copy

Pls read the Meal Pledge Visual identity guidelines attached

Background:
From the organizers: "The numbers of refugees are hard to get your head around. And that’s why you taking this challenge is so important.

By putting yourself in the shoes of just one refugee, for just one week, you’re helping to communicate the suffering caused by this crisis on a human level. At a level we, and those around us, can actually understand."

Extra assets:

Frames and fasteners and other assets can be found here: https://files.vaultdrop.example/s/q4m8zt2lwn5rkx0bc3yhd7pfe916gvja

Requirements
Must have
• Refer to the attached visual design guidelines pdf got the colour ratios

```html
<!DOCTYPE html>
<html lang="en">
<head>
<meta charset="utf-8">
<title>Meal Pledge – Could you live on this much food for 1 week?</title>
<link rel="stylesheet" href="https://fonts.googleapis.com/css2?family=Oswald:wght@500;600&family=Lato:wght@400;700;900&display=swap">
<style>
  :root {
    --red: #8c2632;
    --red-text: #8a2430;
    --white: #f4f4f2;
    --navy: #1b4a75;
    --blue-mid: #2a6fa3;
    --blue-tag: #1a5586;
    --blue-tail: #1c5a8a;
    --blue-light: #6fb3e2;
    --blue-pale: #9fd0f0;
    --ink: #1d3f63;
    --grey-text: #5a6470;
    --line: #1d5b8c;
  }
  * { box-sizing: border-box; margin: 0; padding: 0; }
  html, body { width: 1200px; height: 1200px; overflow: hidden; background: #ffffff; }
  .poster {
    position: absolute; left: 0; top: 0;
    width: 1180px; height: 1180px;
    transform: scale(1.01695); transform-origin: 0 0;
    background: var(--navy);
    overflow: hidden;
    font-family: "Lato", sans-serif;
  }
  .header-band { position: absolute; left: 0; top: 0; width: 1180px; height: 292px; background: var(--red); }
  .header-paper { position: absolute; left: 22px; top: 18px; width: 1136px; height: 274px; background: var(--white); }
  .body-field {
    position: absolute; left: 28px; top: 300px; width: 1124px; height: 732px;
    background: radial-gradient(ellipse at 50% 45%, var(--blue-pale) 0%, var(--blue-light) 55%, #3f86bd 100%);
    box-shadow: 0 0 30px 20px var(--navy) inset;
    border-radius: 6px;
  }
  .brand-mark {
    position: absolute; left: 0; top: 46px; width: 1180px; text-align: center;
    font-family: "Oswald", sans-serif; font-weight: 600; font-size: 80px; line-height: 0.98;
    color: var(--blue-mid); letter-spacing: 3px; text-transform: uppercase;
  }
  .connectors { position: absolute; left: 0; top: 0; }
  .ribbon-tail { position: absolute; }
  .headline {
    position: absolute; left: 146px; top: 245px; width: 886px; height: 107px;
    background: var(--blue-mid);
    display: flex; align-items: center; justify-content: center;
    font-family: "Oswald", sans-serif; font-weight: 500; font-size: 42px;
    color: #ffffff; text-transform: uppercase; letter-spacing: 0.5px;
  }
  .food-tag {
    position: absolute; height: 74px;
    background: var(--blue-tag);
    display: flex; align-items: center; justify-content: center;
    font-weight: 700; font-size: 24px; color: #ffffff; letter-spacing: 1px;
    text-transform: uppercase;
    border-radius: 3px;
  }
  .amount {
    position: absolute; width: 188px; height: 56px;
    background: var(--white);
    clip-path: polygon(0 0, 100% 0, 100% 84%, 50% 100%, 0 84%);
    display: flex; align-items: center; justify-content: center;
    padding-bottom: 4px;
    font-weight: 900; font-size: 28px; color: var(--red-text); letter-spacing: 1px;
  }
  .date-box {
    position: absolute; left: 396px; top: 792px; width: 384px; height: 96px;
    background: var(--blue-tag);
    display: flex; align-items: center; justify-content: center;
    font-weight: 900; font-size: 50px; color: #ffffff; letter-spacing: 2px;
  }
  .signup-label {
    position: absolute; left: 0; top: 908px; width: 1180px; text-align: center;
    font-weight: 700; font-size: 38px; color: var(--ink);
  }
  .signup-url {
    position: absolute; left: 0; top: 962px; width: 1180px; text-align: center;
    font-weight: 700; font-size: 54px; color: var(--ink); letter-spacing: 1px;
  }
  .footer { position: absolute; left: 0; top: 1039px; width: 1180px; height: 106px; background: var(--white); }
  .agency-note {
    position: absolute; left: 46px; top: 20px;
    font-size: 13px; line-height: 16px; color: var(--grey-text); letter-spacing: 1px; text-transform: uppercase;
  }
  .agency-abn {
    position: absolute; left: 46px; top: 58px;
    font-weight: 700; font-size: 25px; color: var(--ink); letter-spacing: 1.5px;
  }
  .partner-name {
    position: absolute; left: 476px; top: 20px;
    font-family: "Lato", sans-serif; font-weight: 900; font-size: 32px; line-height: 1;
    color: var(--red); letter-spacing: 1px; text-transform: uppercase;
  }
  .partner-line {
    position: absolute; left: 476px; top: 64px;
    font-size: 12px; font-weight: 400; color: var(--grey-text); letter-spacing: 1px; text-transform: uppercase;
  }
</style>
</head>
<body>
<main class="poster">
  <div class="header-band"></div>
  <div class="header-paper"></div>
  <div class="body-field"></div>

  <div class="brand-mark">Meal<br>Pledge</div>

  <svg class="ribbon-tail" style="left:88px;top:290px" width="100" height="92" viewBox="0 0 100 92" aria-hidden="true">
    <polygon points="0,82 40,40 0,0 100,0 100,92" fill="var(--blue-tail)"/>
  </svg>
  <svg class="ribbon-tail" style="left:996px;top:290px" width="100" height="92" viewBox="0 0 100 92" aria-hidden="true">
    <polygon points="100,82 60,40 100,0 0,0 0,92" fill="var(--blue-tail)"/>
  </svg>

  <svg class="connectors" width="1180" height="1180" viewBox="0 0 1180 1180" aria-hidden="true">
    <g stroke="var(--line)" stroke-width="2" fill="none">
      <line x1="559" y1="352" x2="559" y2="397"/>
      <line x1="181" y1="397" x2="966" y2="397"/>
      <line x1="181" y1="397" x2="181" y2="482"/>
      <line x1="422" y1="397" x2="422" y2="482"/>
      <line x1="662" y1="397" x2="662" y2="482"/>
      <line x1="966" y1="397" x2="966" y2="482"/>
      <line x1="219" y1="555" x2="219" y2="625"/>
      <line x1="933" y1="555" x2="933" y2="625"/>
      <line x1="376" y1="664" x2="422" y2="664"/>
      <line x1="756" y1="664" x2="797" y2="664"/>
    </g>
  </svg>

  <h1 class="headline">Could you live on this much food for 1 week?</h1>

  <div class="food-tag" style="left:94px;top:480px;width:196px">Rice 1920g</div>
  <div class="food-tag" style="left:328px;top:478px;width:196px">Flour 400g</div>
  <div class="food-tag" style="left:565px;top:481px;width:197px">Lentils 170g</div>
  <div class="food-tag" style="left:802px;top:481px;width:320px">Dried chick peas 85g</div>

  <div class="food-tag" style="left:92px;top:624px;width:286px">Tinned sardines</div>
  <div class="food-tag" style="left:420px;top:624px;width:338px">Tinned kidney beans</div>
  <div class="food-tag" style="left:795px;top:624px;width:288px">Vegetable oil</div>

  <div class="amount" style="left:136px;top:700px">125G</div>
  <div class="amount" style="left:492px;top:700px">400G</div>
  <div class="amount" style="left:840px;top:700px">300ML</div>

  <div class="date-box">JUNE 19-25</div>
  <p class="signup-label">Sign up at</p>
  <p class="signup-url">www.mealpledgeweek.org.au</p>

  <footer class="footer">
    <p class="agency-note">The international aid agency of<br>the Federated Assembly of Parishes.</p>
    <p class="agency-abn">ABN 17 826 305 462</p>
    <p class="partner-name">Kind Harbor</p>
    <p class="partner-line">Standing with people forced from home</p>
  </footer>
</main>
</body>
</html>
```